A4 Tri-fold Brochure for Sedation Dentist Specialist Dr. Marlon and Sedation Dentistry.

I would like to create an A4 tri-fold brochure for our Dental Sedation Specialist Dr. Marlon Vesk. Please carefully select the most suitable highlights from his bio below.

This brochure has two parts. Highlighting what makes Dr. Marlon Vesk unique and trustworthy. Include a picture of him (attached). The second part is about sedation dentistry. All you need to know here: http://www.calmchairplex.com/how-does-sedation-dentistry-work

Avoid making it too wordy.

Meet Dr. Roh Dak Marlon Vesk, DDS

Inspired to Become a Dentist:
As a child, Dr. Marlon Vesk always felt stressed whenever he had to see a dentist. He knew that he wanted to become a dentist to help put patients completely at ease while they experienced quality dental care.

He is passionate about giving patients the healthy, beautiful smiles they deserve. “I find it fulfilling when I can see my patients’ beautiful smiles and how they can finally appreciate the joy of eating with a healthy set of teeth. However, what I love most about my job is the ability to provide a stress-free and comfortable experience at the dentist’s office, particularly for children, through sedation and general anesthesia.”

Educational Achievements:
Before becoming a dentist, Dr. Marlon Vesk earned his undergraduate degree at the Pellridge University of Northern Basin where he received a Bachelor of Medical Science Honor Specialization degree with distinction in biochemistry. He then completed his Doctor of Dental Surgery degree with honors at the Harwick Crest University. While there, he received the Elmer Drayce Medal in his class for outstanding achievement in anesthesia. He then pursued his three-year residency as well as a master’s degree in dental anesthesia at the Harwick Crest University.

So he can provide his patients with the latest in dentistry, Dr. Marlon Vesk enjoys pursuing additional knowledge, particularly in the areas of dental anesthesia as well as advanced technologies in dentistry. He is currently part of the Molar Horizon Circle study club and has enrolled in the Core Rootwork Mini- Residency Program. He also serves as a clinical instructor at the Plenvo Center at the Harwick Crest University.

Association Memberships:
In addition to his academic credentials, Dr. Marlon Vesk is a member of several associations:
The Vantley Board of Dental Surgeons of Quarrow (VBDSQ)
Dental Norvane Guild of Dental Anesthesia (NGDA)
Brisken Forum of Dental Anesthesia (BFDA)
Quarrow Dental Federation (QDF)
Outside the Practice

When he’s not at the practice, Dr. Marlon Vesk enjoys spending time with his wife Wren and their two poodles Pippa and Biscuit, who are spoiled rotten! “Wren and I love taking our dogs out on hikes and to the dog park on weekends. I also enjoy a wide range of activities from model building and playing the piano to soccer, gym and archery.” He stays fit by working out at the local Fitwell gym, and he likes to walk in Ashbury Lake Park and Dunmore Field Park.

Dr. Marlon Vesk considers himself to be a kid at heart. He is a big fan of superheroes and animated movies. “I get really excited about any upcoming superhero or Zentry Lumo movies. Till this day, I still collect superhero toy figures.”

He supports the BrightCot Foundation as well as the Quarrow League for the Protection of Animal Welfare (LPAW).

Experience outstanding dental care with our highly skilled dentist. Contact us today to schedule an appointment with Dr. Marlon Vesk! He speaks English, Cantonese, and Mandarin.

Target Market(s)

Mothers with young kids.

Industry/Entity Type

Dental

Font styles to use
Sans Serif

Requirements
Should not have
• Prices

```html
<!DOCTYPE html>
<html lang="en">
<head>
<meta charset="utf-8">
<title>Sedation Dentistry Tri-fold Brochure – Dr. Marlon Vesk</title>
<link href="https://fonts.googleapis.com/css2?family=Open+Sans:ital,wght@0,400;0,600;0,700;1,600&family=Roboto+Condensed:wght@300;400;700&display=swap" rel="stylesheet">
<style>
:root{
  --teal:#1b86a3;
  --teal-dark:#0d4f63;
  --teal-deep:#0a3b4b;
  --teal-light:#2bb3d1;
  --orange:#f7941d;
  --red:#d8322c;
  --ink:#4a4a4a;
  --paper:#ffffff;
  --paper-grey:#f2f2f2;
  --stage:#2a2a2a;
}
*{box-sizing:border-box;margin:0;padding:0}
html,body{width:1121px;height:1200px;overflow:hidden;background:var(--stage)}
body{position:relative;font-family:"Open Sans",Arial,sans-serif;color:var(--ink)}
.sheet{position:absolute;left:20px;width:1081px;height:550px;background:var(--paper);overflow:hidden;display:flex}
.sheet--outer{top:35px}
.sheet--inside{top:615px}
.panel{position:relative;width:360px;height:100%;overflow:hidden}
.panel + .panel{width:360.5px}
.head{font-family:"Roboto Condensed",Arial,sans-serif;text-transform:uppercase}
p,li{font-size:10.5px;line-height:1.42}

/* outer left: types */
.types{background:var(--paper-grey);padding:18px 24px 0 20px}
.types__title{color:var(--orange);font-size:16px;font-weight:700;border-top:2px solid var(--orange);padding-top:7px;margin-bottom:11px}
.method{display:flex;gap:14px;margin-bottom:10px}
.method__icon{flex:0 0 46px;height:50px;border-radius:6px;background:linear-gradient(#e9ecee,#cfd6da)}
.method__name{font-family:"Roboto Condensed",Arial,sans-serif;color:var(--teal);font-weight:700;font-size:13.5px;text-transform:uppercase;margin-bottom:3px}
.method p{font-size:10px;line-height:1.35;margin-bottom:4px}
.method ul{list-style:none;padding-left:10px;margin-bottom:4px}
.method ul li{font-size:10px;line-height:1.35}
.method ul li::before{content:"• ";color:var(--teal)}
.wave-foot{position:absolute;left:0;bottom:0;width:100%;height:60px}

/* outer middle */
.pattern{position:absolute;left:0;top:0;width:100%;height:270px;background:radial-gradient(circle at 30% 20%,#1f5a6a,#0b2a34 75%)}
.swoosh{position:absolute;left:0;top:170px;width:721px;height:170px}
.sources{position:absolute;left:24px;top:370px;right:24px}
.sources__title{color:var(--orange);font-family:"Roboto Condensed",Arial,sans-serif;font-weight:700;font-size:12px;margin-bottom:8px}
.sources p{font-size:9px;line-height:1.35;margin-bottom:8px;word-break:break-all}

/* outer right */
.portrait{position:absolute;left:0;top:0;width:100%;height:300px;background:linear-gradient(160deg,#e8ecef,#b9c4cc 60%,#1c3a4a)}
.meet{position:absolute;right:0;top:22px;background:var(--orange);color:#fff;font-family:"Roboto Condensed",Arial,sans-serif;font-weight:700;font-size:20px;padding:8px 16px 8px 20px}
.nameblock{position:absolute;left:36px;right:24px;top:410px;text-align:right}
.nameblock__role{color:var(--orange);font-weight:300;font-size:20px;border-top:1px solid var(--orange);padding-top:6px}
.nameblock__name{color:var(--teal-dark);font-weight:700;font-size:30px;line-height:1.05;margin-top:4px}

/* inside left */
.bio{background:linear-gradient(180deg,var(--teal) 0%,var(--teal-dark) 100%);color:#fff;padding:20px 24px}
.bio__head{display:flex;align-items:center;gap:10px;margin-bottom:10px}
.bio__head::before{content:"";flex:0 0 28px;height:28px;border:2px solid #fff;border-radius:50%}
.bio__title{font-size:13px;font-weight:300;line-height:1.1}
.bio__title b{display:block;font-size:19px;font-weight:700}
.bio p{font-size:10px;margin-bottom:7px;color:#e8f5f9}
.bio__section{margin-top:12px}

/* inside middle */
.assoc__header{background:var(--teal-dark);color:#fff;padding:20px 24px 18px;height:96px}
.assoc__header .bio__head{margin-bottom:0}
.assoc__body{padding:14px 24px 0}
.assoc__body p{margin-bottom:6px}
.assoc__body ul{list-style:none;margin-bottom:8px}
.assoc__body li{font-size:10px;color:var(--teal)}
.callout{margin:8px 24px 0;background:var(--orange);color:#fff;padding:10px 14px}
.callout p{font-style:italic;font-weight:600;font-size:10.5px}
.smile{position:absolute;left:24px;right:24px;top:392px;height:120px;background:linear-gradient(90deg,#e9d6cf,#f6f2ee 50%,#c9a8a0)}

/* inside right */
.benefits{padding:24px 26px 0 24px}
.benefits__lead{border-left:4px solid var(--teal);padding-left:10px;color:var(--teal);font-weight:300;font-size:17px;line-height:1.1}
.benefits__lead b{display:block;font-size:30px;font-weight:700;line-height:1}
.benefits__title{color:var(--orange);font-weight:700;font-size:14px;margin:14px 0 12px;border-bottom:1px solid var(--orange);padding-bottom:4px}
.benefit{display:flex;gap:14px;margin-bottom:11px}
.benefit svg{flex:0 0 30px;height:30px}
.benefit__name{color:var(--red);font-family:"Roboto Condensed",Arial,sans-serif;font-weight:700;font-size:12px;text-transform:uppercase;margin-bottom:2px}
.benefit p{font-size:10px;line-height:1.35;margin-bottom:2px}
</style>
</head>
<body>

<section class="sheet sheet--outer">
  <div class="panel types">
    <h2 class="head types__title">Types of Dental Sedation</h2>
    <div class="method">
      <div class="method__icon" role="img" aria-label="Illustration of a gas canister and mask"></div>
      <div>
        <h3 class="method__name">Nitrous Oxide (Laughing Gas)</h3>
        <p>Your dentist gives you a mask and you breath in nitrous oxide</p>
        <p>Helps you feel more relaxed, and wears off quickly</p>
        <p>Sometimes used in combination with other methods</p>
      </div>
    </div>
    <div class="method">
      <div class="method__icon" role="img" aria-label="Illustration of pills"></div>
      <div>
        <h3 class="method__name">Oral Conscious</h3>
        <p>A popular and effective method of sedation dentistry</p>
        <p>You'll take a pill, and the dental work only begins once it's taken effect</p>
        <p>Even though you're sedated, you'll be able to respond to questions</p>
      </div>
    </div>
    <div class="method">
      <div class="method__icon" role="img" aria-label="Illustration of an IV drip bag"></div>
      <div>
        <h3 class="method__name">IV</h3>
        <p>Sedative is administered intravenously, giving you a precise level of relaxation</p>
        <p>Performed by a Board Certified Anesthesiologist</p>
        <p>Depending on the procedure, you may be sedated to different levels</p>
        <ul>
          <li>You may be conscious and able to respond to questions</li>
          <li>You may be sedated more deeply if need be</li>
        </ul>
        <p>Bring a friend or family member to drive you to and from the procedure</p>
      </div>
    </div>
    <svg class="wave-foot" viewBox="0 0 360 60" preserveAspectRatio="none">
      <path d="M0 30 C120 5 240 55 360 20 L360 60 L0 60Z" fill="var(--teal-light)"/>
      <path d="M0 42 C120 20 240 62 360 35 L360 60 L0 60Z" fill="var(--teal-dark)"/>
    </svg>
  </div>

  <div class="panel">
    <div class="pattern" role="img" aria-label="Dark teal pattern of rounded squares"></div>
    <div class="sources">
      <h4 class="head sources__title">Sources:</h4>
      <p>http://www.calmchairplex.com/services/iv-sedation.aspx</p>
      <p>http://www.toothpathguide.com/sedation/</p>
      <p>http://www.healthlumenmd.com/oral-health/sedation-dentistry-can-you-really-relax-in-the-dentists-chair</p>
    </div>
  </div>

  <div class="panel">
    <div class="portrait" role="img" aria-label="Portrait photo of Dr. Marlon Vesk in navy scrubs with a stethoscope"></div>
    <div class="meet">MEET</div>
    <div class="nameblock">
      <p class="head nameblock__role">Dental Sedation Specialist</p>
      <h1 class="head nameblock__name">Dr. Roh Dak<br>Marlon Vesk, DDS</h1>
    </div>
  </div>

  <svg class="swoosh" viewBox="0 0 721 170" preserveAspectRatio="none" style="left:360px">
    <path d="M0 100 C150 40 260 20 400 90 C520 150 620 130 721 80 L721 170 L0 170Z" fill="#fff"/>
    <path d="M0 70 C160 10 280 20 420 70 C540 110 640 100 721 60 L721 90 C640 125 540 135 420 100 C280 55 160 55 0 110Z" fill="var(--teal)"/>
    <path d="M0 110 C160 55 280 60 420 100 C540 135 640 125 721 90 L721 100 C640 140 540 150 420 115 C280 75 160 75 0 125Z" fill="var(--teal-light)"/>
  </svg>
  <svg class="swoosh" viewBox="0 0 360 60" preserveAspectRatio="none" style="left:721px;top:490px;width:360px;height:60px">
    <path d="M0 35 C120 60 240 10 360 25 L360 60 L0 60Z" fill="var(--teal-light)"/>
    <path d="M0 48 C120 65 240 25 360 40 L360 60 L0 60Z" fill="var(--teal-dark)"/>
  </svg>
</section>

<section class="sheet sheet--inside">
  <div class="panel bio">
    <div class="bio__head"><h2 class="head bio__title">Inspired to become a <b>Dentist:</b></h2></div>
    <p>As a child, Dr. Marlon Vesk always felt stressed whenever he had to see a dentist. He knew that he wanted to become a dentist to help put patients completely at ease while they experienced quality dental care.</p>
    <p>He is passionate about giving patients the healthy, beautiful smiles they deserve. “I find it fulfilling when I can see my patients’ beautiful smiles and how they can finally appreciate the joy of eating with a healthy set of teeth. However, what I love most about my job is the ability to provide a stress-free and comfortable experience at the dentist’s office, particularly for children, through sedation and general anesthesia.”</p>
    <div class="bio__section">
      <div class="bio__head"><h2 class="head bio__title">Educational <b>Achievements:</b></h2></div>
      <p>Before becoming a dentist, Dr. Marlon Vesk earned his undergraduate degree at the Pellridge University of Northern Basin where he received a Bachelor of Medical Science Honor Specialization degree with distinction in biochemistry. He then completed his Doctor of Dental Surgery degree with honors at the Harwick Crest University. While there, he received the Elmer Drayce Medal in his class for outstanding achievement in anesthesia. He then pursued his three-year residency as well as a master’s degree in dental anesthesia at the Harwick Crest University.</p>
      <p>So he can provide his patients with the latest in dentistry, Dr. Marlon Vesk enjoys pursuing additional knowledge. He is currently part of the Molar Horizon Circle study club and has enrolled in the Core Rootwork Mini- Residency Program. He also serves as a clinical instructor at the Plenvo Center at the Harwick Crest University.</p>
    </div>
  </div>

  <div class="panel">
    <div class="assoc__header">
      <div class="bio__head"><h2 class="head bio__title">Association <b>Memberships:</b></h2></div>
    </div>
    <div class="assoc__body">
      <p><b>In addition to his academic credentials, Dr. Marlon Vesk is a member of several associations:</b></p>
      <ul>
        <li>The Vantley Board of Dental Surgeons of Quarrow (VBDSQ)</li>
        <li>Dental Norvane Guild of Dental Anesthesia (NGDA)</li>
        <li>Brisken Forum of Dental Anesthesia (BFDA)</li>
        <li>Quarrow Dental Federation (QDF)</li>
      </ul>
      <p>Dr. Marlon Vesk considers himself to be a kid at heart. He supports the BrightCot Foundation as well as the Quarrow League for the Protection of Animal Welfare (LPAW).</p>
    </div>
    <div class="callout">
      <p>Experience outstanding dental care with our highly skilled dentist. Contact us today to schedule an appointment with Dr. Marlon Vesk! He speaks English, Cantonese, and Mandarin.</p>
    </div>
    <div class="smile" role="img" aria-label="Close-up photo of a smile with a dental mirror"></div>
    <svg class="wave-foot" viewBox="0 0 360 60" preserveAspectRatio="none">
      <path d="M0 25 C120 55 240 5 360 30 L360 60 L0 60Z" fill="var(--teal-light)"/>
      <path d="M0 40 C120 65 240 20 360 45 L360 60 L0 60Z" fill="var(--teal-dark)"/>
    </svg>
  </div>

  <div class="panel benefits">
    <h2 class="head benefits__lead">Relaxing in the dentist's chair with <b>Sedation Dentistry</b></h2>
    <h3 class="head benefits__title">Benefits of Sedation Dentistry</h3>
    <div class="benefit">
      <svg viewBox="0 0 30 30"><circle cx="15" cy="15" r="12" fill="none" stroke="var(--red)" stroke-width="3"/><path d="M15 8v7l5 3" fill="none" stroke="var(--red)" stroke-width="2.5" stroke-linecap="round"/></svg>
      <div><h4 class="benefit__name">Time</h4>
        <p>Dental sedation can make it feel like less time has passed</p>
        <p>Ideal if you need to get a lot of dental work done</p></div>
    </div>
    <div class="benefit">
      <svg viewBox="0 0 30 30"><path d="M6 17l6 6 12-14" fill="none" stroke="var(--red)" stroke-width="4" stroke-linecap="round" stroke-linejoin="round"/></svg>
      <div><h4 class="benefit__name">Convenience</h4>
        <p>If you need a great deal of work, you can get more accomplished in one visit</p>
        <p>Reduces the need for multiple visits to the dentist</p></div>
    </div>
    <div class="benefit">
      <svg viewBox="0 0 30 30"><path d="M3 14 C9 8 21 8 27 14 C21 22 9 22 3 14Z" fill="var(--red)"/><path d="M7 14 C12 16 18 16 23 14" fill="none" stroke="#fff" stroke-width="1.5"/></svg>
      <div><h4 class="benefit__name">Comfort</h4>
        <p>Sedation allows you to relax during dental treatments</p>
        <p>Especially important if you have anxieties or fears about going to the dentist</p></div>
    </div>
    <div class="benefit">
      <svg viewBox="0 0 30 30"><path d="M15 26 C5 18 2 13 4 8 C6 4 12 4 15 9 C18 4 24 4 26 8 C28 13 25 18 15 26Z" fill="var(--red)"/></svg>
      <div><h4 class="benefit__name">Health</h4>
        <p>When you're not afraid of the dentist, you're more likely to go regularly</p>
        <p>Helps keep your oral health in good standing since you won't avoid visits</p></div>
    </div>
    <svg class="wave-foot" viewBox="0 0 360 60" preserveAspectRatio="none">
      <path d="M0 30 C120 5 240 55 360 20 L360 60 L0 60Z" fill="var(--teal-light)"/>
      <path d="M0 45 C120 20 240 62 360 38 L360 60 L0 60Z" fill="var(--teal-dark)"/>
    </svg>
  </div>
</section>

</body>
</html>
```